Verdanix Medical Business Card

Create a high class Business card for Medical Aesthetics and Wellness Practice called Verdanix Medical Aesthetics and Wellness as per the logo attached.
Addresss is: 418 Harlan Brook Road Suite 312 Melville, New York 11093
Phone (555)204-7391 IG @verdanix_medical
Verdanixmedical.example

I need 5 different name configurations
1) Dr. Theo Valcourt
Aesthetics and Wellness Specialist
Medical Director

2) Rosalind Pettinger, NP
Clinical Nurse Manager

3) Marla Vostrik, RN
Aesthetic Nurse Specialist

4) Petra Halvesen, RN

5) Dana Kowbeck, L.E.
Senior Licensed Esthetician

Target Market(s)

22-55 Females

Industry/Entity Type

Medical Spa and Wellness

Contact Information for Business Card

Logo, address, phone, web, instagram, providers name

Requirements
Must have
• Attractive classy modern look

```html
<!DOCTYPE html>
<html lang="en">
<head>
<meta charset="utf-8">
<title>Verdanix Medical Business Card</title>
<link rel="stylesheet" href="https://fonts.googleapis.com/css2?family=Cinzel:wght@700&family=Cormorant+Garamond:wght@300&family=Cormorant+SC:wght@500&family=Josefin+Sans:wght@400&display=swap">
<style>
  :root {
    --page: #ebdfe0;
    --ink: #ffffff;
    --ink-soft: #e9e2e2;
    --card-back: #2a0202;
    --card-front-dark: #060102;
    --card-front-red: #4a0406;
  }
  html, body {
    margin: 0;
    padding: 0;
    width: 1200px;
    height: 1110px;
    overflow: hidden;
    background: var(--page);
  }
  .canvas {
    position: relative;
    width: 1200px;
    height: 1110px;
  }
  .card {
    position: absolute;
    width: 754px;
    height: 443px;
    box-sizing: border-box;
    color: var(--ink);
  }
  .card-front {
    left: 75px;
    top: 75px;
    overflow: hidden;
  }
  .front-backdrop {
    position: absolute;
    inset: 0;
    display: block;
  }
  .brand {
    position: absolute;
    left: 0;
    right: 0;
    top: 218px;
    text-align: center;
  }
  .brand-name {
    font-family: "Cormorant Garamond", serif;
    font-weight: 300;
    font-size: 62px;
    letter-spacing: 5px;
    line-height: 1;
    margin: 0;
    color: var(--ink-soft);
  }
  .brand-tagline {
    font-family: "Cormorant Garamond", serif;
    font-weight: 300;
    font-size: 19px;
    letter-spacing: 1.2px;
    text-transform: uppercase;
    margin: 16px 0 0;
    color: var(--ink-soft);
  }
  .brand-city {
    font-family: "Cormorant Garamond", serif;
    font-weight: 300;
    font-size: 13px;
    letter-spacing: 7px;
    text-transform: uppercase;
    margin: 12px 0 0;
    color: var(--ink-soft);
  }
  .card-back {
    left: 371px;
    top: 590px;
    background: var(--card-back);
    text-align: center;
  }
  .person-name {
    position: absolute;
    left: 0;
    right: 0;
    top: 46px;
    margin: 0;
    font-family: "Cinzel", serif;
    font-weight: 700;
    font-size: 39px;
    line-height: 1;
    letter-spacing: 0.5px;
  }
  .person-title {
    position: absolute;
    left: 0;
    right: 0;
    top: 98px;
    margin: 0;
    font-family: "Cormorant SC", serif;
    font-weight: 500;
    font-size: 35px;
    line-height: 1;
    letter-spacing: 3.5px;
  }
  .contact-list {
    position: absolute;
    left: 0;
    right: 0;
    top: 220px;
    margin: 0;
    padding: 0;
    list-style: none;
    font-family: "Josefin Sans", sans-serif;
    font-size: 17px;
    letter-spacing: 1px;
  }
  .contact-list li {
    height: 47.5px;
    line-height: 26px;
  }
</style>
</head>
<body>
<main class="canvas">
  <section class="card card-front">
    <svg class="front-backdrop" width="754" height="443" viewBox="0 0 754 443" role="img" aria-label="Abstract background of dark crimson angular light shards on black">
      <defs>
        <radialGradient id="glow-left" cx="0.15" cy="0.7" r="0.7">
          <stop offset="0" stop-color="var(--card-front-red)"/>
          <stop offset="1" stop-color="var(--card-front-dark)"/>
        </radialGradient>
        <radialGradient id="glow-right" cx="0.8" cy="0.25" r="0.5">
          <stop offset="0" stop-color="#3a0305" stop-opacity="0.8"/>
          <stop offset="1" stop-color="#3a0305" stop-opacity="0"/>
        </radialGradient>
      </defs>
      <rect width="754" height="443" fill="url(#glow-left)"/>
      <rect width="754" height="443" fill="url(#glow-right)"/>
    </svg>
    <div class="brand">
      <p class="brand-name">Verdanix</p>
      <p class="brand-tagline">Medical Aesthetics and Wellness</p>
      <p class="brand-city">New York</p>
    </div>
  </section>

  <section class="card card-back">
    <h1 class="person-name">ROSALIND PETTINGER, NP</h1>
    <p class="person-title">Clinical Nurse Manager</p>
    <ul class="contact-list">
      <li>(555)204-7391</li>
      <li>@verdanix_medical</li>
      <li>www.verdanixmedical.example</li>
      <li>418 Harlan Brook Road Suite 312 Melville, New York 11093</li>
    </ul>
  </section>
</main>
</body>
</html>
```